Brackenly.com Postcard

We want to create a postcard, which is going to be mailed out to 6k managers at Hospitals throughout the USA.

I attached a rough draft of what I want the postcard to look like, but want it to look much better. The postcard size is 5.47" * 4.21"

```html
<!DOCTYPE html>
<html lang="en">
<head>
<meta charset="utf-8">
<title>Brackenly Medical Postcard</title>
<link rel="stylesheet" href="https://fonts.googleapis.com/css2?family=Jost:wght@400;500;700&family=Anton&display=swap">
<style>
  :root {
    --navy: #141d5c;
    --blue: #4a6db3;
    --sky: #a9c1d6;
    --red: #e3140f;
    --ink: #111111;
    --backdrop: #e1e1e1;
    --paper: #ffffff;
    --faint: #ececec;
    --rule: #555555;
  }
  * { box-sizing: border-box; margin: 0; padding: 0; }
  html, body { width: 1037px; height: 1200px; overflow: hidden; }
  body { background: var(--backdrop); position: relative; font-family: "Jost", sans-serif; color: var(--navy); }

  .card { position: absolute; background: var(--paper); box-shadow: 0 3px 10px rgba(0,0,0,.35); overflow: hidden; }
  .card-front { left: 174px; top: 39px; width: 682px; height: 524px; }
  .card-back { left: 166px; top: 595px; width: 697px; height: 540px; }
  .swoosh { position: absolute; left: 0; top: 0; }

  .brand { position: absolute; display: flex; align-items: center; gap: 10px; color: var(--navy); font-weight: 500; letter-spacing: 1px; white-space: nowrap; }
  .brand-dot { width: 34px; height: 34px; border-radius: 50%; background: var(--navy); flex: none; }
  .card-front .brand { left: 146px; top: 42px; font-size: 40px; }
  .card-back .brand { left: 70px; top: 76px; font-size: 44px; }
  .brand-faint { position: absolute; left: 80px; top: 470px; font-size: 44px; color: var(--faint); font-weight: 500; letter-spacing: 1px; display: flex; gap: 10px; align-items: center; white-space: nowrap; }
  .brand-faint .brand-dot { background: var(--faint); }

  .rule-fade { position: absolute; height: 3px; background: linear-gradient(90deg, transparent, var(--rule) 25%, var(--rule) 75%, transparent); }

  .headline { position: absolute; font-family: "Anton", sans-serif; color: var(--red); text-align: center; letter-spacing: .3px; }
  .front-headline { left: 0; width: 682px; top: 112px; font-size: 36px; line-height: 44px; }
  .front-call { position: absolute; left: 0; width: 682px; top: 186px; text-align: center; font-weight: 700; font-size: 32px; color: var(--navy); }

  .front-body { position: absolute; left: 48px; top: 264px; width: 332px; font-size: 20px; line-height: 23px; text-align: justify; letter-spacing: .5px; color: var(--navy); }
  .product-photo { position: absolute; left: 400px; top: 228px; width: 240px; height: 225px; border-radius: 10px;
    background: linear-gradient(160deg, #e8ecef 0%, #c9d0d6 55%, #d9b49b 100%); }
  .front-cta { position: absolute; left: 49px; top: 458px; font-size: 26px; color: var(--ink); white-space: nowrap; }
  .front-cta strong { color: var(--navy); font-weight: 700; }

  .return-address { position: absolute; right: 191px; top: 22px; text-align: right; font-size: 15px; line-height: 20px; color: var(--ink); font-style: normal; white-space: nowrap; }
  .stamp-box { position: absolute; left: 526px; top: 38px; width: 125px; height: 135px; border: 1px solid #999; }
  .back-headline { left: 0; width: 350px; top: 178px; font-size: 37px; line-height: 50px; }
  .back-contact { position: absolute; left: 0; width: 350px; top: 312px; text-align: center; color: var(--ink); }
  .back-contact .phone { font-weight: 700; font-size: 26px; line-height: 30px; }
  .back-contact .line { font-size: 20px; line-height: 27px; }
  .mail-line { position: absolute; left: 385px; width: 266px; height: 1px; background: #333; }
</style>
</head>
<body>

<section class="card card-front">
  <svg class="swoosh" width="682" height="524" viewBox="0 0 682 524" aria-hidden="true">
    <path d="M0 0 H112 C60 25 22 60 0 105 Z" fill="var(--blue)"/>
    <path d="M168 0 C80 40 20 150 0 290 V190 C25 100 80 30 130 0 Z" fill="var(--sky)"/>
    <path d="M682 420 V524 H590 C630 500 665 465 682 420 Z" fill="var(--blue)"/>
    <path d="M682 300 C660 420 600 490 520 524 H560 C640 480 675 410 682 350 Z" fill="var(--sky)"/>
  </svg>

  <div class="brand"><span class="brand-dot"></span>Brackenly Medical</div>
  <div class="rule-fade" style="left:60px;width:600px;top:99px"></div>
  <h1 class="headline front-headline">Looking To Sell Your Infusion IV Pumps?</h1>
  <div class="rule-fade" style="left:60px;width:600px;top:163px"></div>
  <p class="front-call">Call (555) 014 2270</p>

  <p class="front-body">Brackenly Medical will purchase your infusion iv pumps. We will buy all of your quality iv pumps. We offer competitive pricing and will purchase from companies and individuals.</p>
  <div class="product-photo" role="img" aria-label="Photo of a hand holding an infusion IV pump"></div>

  <p class="front-cta">Sell infusion pumps to <strong>Brackenly Medical</strong> today!</p>
</section>

<section class="card card-back">
  <svg class="swoosh" width="697" height="540" viewBox="0 0 697 540" aria-hidden="true">
    <path d="M0 0 H100 C55 25 20 60 0 100 Z" fill="var(--blue)"/>
    <path d="M150 0 C70 40 15 140 0 260 V180 C20 95 70 30 115 0 Z" fill="var(--sky)"/>
    <path d="M335 330 V445 H220 C280 420 320 380 335 330 Z" fill="var(--blue)"/>
    <path d="M335 162 C330 300 280 400 160 445 H215 C300 410 335 330 335 250 Z" fill="var(--sky)"/>
  </svg>

  <address class="return-address">PO Box 3092<br>Larkfield, NC 27000</address>
  <div class="stamp-box"></div>
  <div class="brand"><span class="brand-dot"></span>Brackenly Medical</div>

  <div class="rule-fade" style="left:30px;width:300px;top:163px"></div>
  <h2 class="headline back-headline">WE BUY<br>INFUSION IV PUMPS</h2>
  <div class="rule-fade" style="left:20px;width:310px;top:286px"></div>

  <div class="back-contact">
    <p class="phone">555 014 2270</p>
    <p class="line">sales@brackenly.com</p>
    <p class="line">www.brackenly.com</p>
  </div>

  <div class="mail-line" style="top:257px"></div>
  <div class="mail-line" style="top:303px"></div>
  <div class="mail-line" style="top:354px"></div>

  <div class="brand-faint"><span class="brand-dot"></span>Brackenly Medical</div>
</section>

</body>
</html>
```